Book cover design, title is "Go Solo Now: How to Swap Your Salary in 10 Seasons"

Design a cover for a book about freelancing. Example of my previous book's cover attached. Book title is "Go Solo Now: How to Swap Your Salary in 10 Seasons". Looking to target people who have a 9-5 job but are seeking to try out freelancing as a way to supplement income and eventually quit their day job.

Target Market(s)

Looking to target people who have a 9-5 job but are seeking to try out freelancing as a way to supplement income and eventually quit their day job.

Industry/Entity Type

Consulting

Font styles to use
Serif
Sans Serif

Colors

Designer to choose colors to be used in the design.

Requirements
Must have
• I love these books covers...
• https://www.pagelodge.example/Tame-Notebin-Casual-Sorting-Settled-ebook/dp/Q71MWRTZPA/ref=asap_bc?ie=UTF8
• https://www.pagelodge.example/Bright-Dawn-Scribes-Drafting-Doubles/dp/5830617294/ref=asap_bc?ie=UTF8
• https://www.pagelodge.example/Way-Pen-Factual-eBook-Weeks-ebook/dp/Q93KT41ZXN/ref=asap_bc?ie=UTF8
• https://www.pagelodge.example/Ritual-Piling-Tiny-Shifts-Moments/dp/6027158392/ref=asap_bc?ie=UTF8
• https://www.pagelodge.example/Boost-Each-Hour-Core-ebook/dp/Q82WFN6JTM/ref=asap_bc?ie=UTF8
• https://www.pagelodge.example/Artisan-Co-Total-Thriving-Gig-ebook/dp/Q66813XKVR/ref=sr_1_4?ie=UTF8&qid=2738405519&sr=8-4&keywords=freelancing
Should not have
• Don't submit 3D renderings, just the front cover image please.

```html
<!DOCTYPE html>
<html lang="en">
<head>
<meta charset="utf-8">
<title>Go Solo Now: How to Swap Your Salary in 10 Seasons</title>
<link href="https://fonts.googleapis.com/css2?family=VT323&family=Audiowide&display=swap" rel="stylesheet">
<style>
  :root {
    --sky: #7ecfd4;
    --grid-line: rgba(255, 255, 255, 0.22);
    --glow: #e6f6f7;
    --ink: #1f3e50;
    --navy-band: #1e394b;
    --step-top: #dcdcdf;
    --step-shade: #c4c4c9;
    --gold: #e8bf6a;
    --crimson: #e1365a;
    --scene-main: #2a5b6c;
    --scene-soft: #8fd3d8;
  }
  * { margin: 0; padding: 0; box-sizing: border-box; }
  html, body { width: 880px; height: 1200px; overflow: hidden; background: var(--sky); }

  .cover {
    position: relative;
    width: 880px;
    height: 1200px;
    overflow: hidden;
    background-color: var(--sky);
    background-image:
      radial-gradient(circle at 440px 560px, var(--glow) 0, rgba(230, 246, 247, 0.6) 120px, rgba(126, 207, 212, 0) 280px),
      linear-gradient(var(--grid-line) 1px, transparent 1px),
      linear-gradient(90deg, var(--grid-line) 1px, transparent 1px);
    background-size: 100% 100%, 32px 32px, 32px 32px;
  }

  .title {
    position: absolute;
    top: 0;
    left: 0;
    width: 100%;
    text-align: center;
    font-family: "VT323", monospace;
    color: var(--ink);
    line-height: 1;
  }
  .title-line {
    display: block;
    font-size: 176px;
    letter-spacing: 2px;
  }
  .title-line--first { margin-top: 4px; }
  .title-line--second { margin-top: 26px; }

  .hero-art {
    position: absolute;
    left: 278px;
    top: 436px;
    width: 320px;
    height: 292px;
    border-radius: 14px;
    background: linear-gradient(180deg, var(--scene-soft) 0%, var(--scene-main) 100%);
  }

  .steps {
    position: absolute;
    left: 0;
    top: 0;
  }

  .step-label {
    position: absolute;
    left: 0;
    width: 100%;
    text-align: center;
    font-family: "Audiowide", sans-serif;
    line-height: 1;
  }
  .step-label--top {
    top: 783px;
    font-size: 40px;
    color: var(--sky);
    text-shadow: 2px 2px 0 var(--ink);
  }
  .step-label--middle {
    top: 900px;
    font-size: 72px;
    color: var(--gold);
    text-shadow: 3px 3px 0 var(--ink);
  }
  .step-label--base {
    top: 1064px;
    font-size: 90px;
    color: var(--crimson);
    text-shadow: 4px 4px 0 #0f2230;
  }
</style>
</head>
<body>
<main class="cover">
  <h1 class="title">
    <span class="title-line title-line--first">Go Solo</span>
    <span class="title-line title-line--second">Now</span>
  </h1>

  <div class="hero-art" role="img" aria-label="Illustration of a rocket launching out of an open laptop screen on a cloud of smoke"></div>

  <svg class="steps" width="880" height="1200" viewBox="0 0 880 1200" aria-hidden="true">
    <defs>
      <linearGradient id="stepFace" x1="0" y1="0" x2="0" y2="1">
        <stop offset="0" stop-color="var(--step-shade)"/>
        <stop offset="1" stop-color="var(--step-top)"/>
      </linearGradient>
    </defs>
    <polygon class="step-face" points="240,700 640,700 661,764 216,764" fill="url(#stepFace)"/>
    <rect class="step-riser step-riser--gold" x="216" y="764" width="445" height="82" fill="var(--gold)"/>
    <polygon class="step-face" points="216,846 661,846 752,886 128,886" fill="url(#stepFace)"/>
    <rect class="step-riser step-riser--crimson" x="128" y="886" width="624" height="107" fill="var(--crimson)"/>
    <polygon class="step-face" points="128,993 752,993 880,1040 0,1040" fill="url(#stepFace)"/>
    <rect class="base-band" x="0" y="1040" width="880" height="160" fill="var(--navy-band)"/>
  </svg>

  <p class="step-label step-label--top">How to Swap</p>
  <p class="step-label step-label--middle">Your Salary</p>
  <p class="step-label step-label--base">in 10 Seasons</p>
</main>
</body>
</html>
```